Web Design Project

I need a web site for and medical spa aesthetics
We offer plumavex corvanel and laser photo facials
http://www.briefhall-example.com/design/4907316
Updates
Cosmetic Treatments
- Tensira/Calvane
- Fillers
- Liquid Face Lift
- Skin Tightening
- Skin Complexion Analysis
- Anti-Aging Treatments
- Wrinkle Reduction
- Sclerotherapy- Leg Veins
Laser & Pulsed Light
- Brown Age Spot Removal
- Painless Laser Hair Removal
- Laser Skin Resurfacing
- Facial Redness Reduction
- Tattoo Removal
Target Market(s)
My target market is women over 40 as well as men over 50
Industry/Entity Type
Medical
Requirements
Must have
- Pleasuring to the eye for both males and females
The name of the spa us velorin aesthetics and laser
Nice to have
- Should be also viewable on mobile Zelfon quillos etc
And should have scheduling calendar
Should not have
- Needs to be beautiful and elegant no leaves or flowers like
Every other site

```html
<!DOCTYPE html>
<html lang="en">
<head>
<meta charset="utf-8">
<title>Velorin Aesthetics and Laser</title>
<link href="https://fonts.googleapis.com/css2?family=Arimo:ital,wght@0,400;0,700;1,400&display=swap" rel="stylesheet">
<style>
:root{
  --backdrop:#b9865c;
  --page:#ffffff;
  --blue:#2f6aa0;
  --blue-dark:#245684;
  --nav-top:#6a9ccb;
  --nav-bottom:#34689c;
  --orange:#e8531b;
  --orange-light:#f08a5a;
  --slate-top:#7189be;
  --slate-bottom:#3c5a98;
  --text:#333333;
  --muted:#777777;
  --sky:#dcecf7;
  --footer-top:#3a3a3a;
  --footer-bottom:#151515;
}
*{margin:0;padding:0;box-sizing:border-box}
html,body{width:1200px;height:1148px;overflow:hidden}
body{background:var(--backdrop);font-family:"Arimo",Arial,sans-serif;color:var(--text)}
.stage{width:1150px;height:1100px;position:relative;transform:scale(1.04348);transform-origin:0 0}
.site{position:absolute;left:86px;top:26px;width:978px;height:1029px;background:var(--page);box-shadow:0 2px 10px rgba(0,0,0,.35)}
.brand{position:absolute;left:14px;top:14px;display:flex;flex-direction:column;color:var(--blue);font-weight:700}
.brand-mark{width:30px;height:30px;border-radius:50%;background:var(--orange);margin:0 0 8px 80px}
.brand-name{font-size:44px;letter-spacing:1px;line-height:42px}
.brand-tag{font-size:13px;letter-spacing:1.4px;margin-top:2px}
.search{position:absolute;left:777px;top:23px;width:192px;height:32px;border:1px solid #cfcfcf;font-size:11px;color:#888;padding:10px 11px}
.search svg{position:absolute;right:8px;top:7px}
.contact{position:absolute;top:70px;font-size:14px;line-height:22px;color:var(--blue)}
.contact.address{right:206px;text-align:right}
.contact.lines{left:798px;border-left:1px solid #ccc;padding-left:13px;left:785px}
.contact .hl{color:var(--orange)}
.nav{position:absolute;left:9px;top:139px;width:960px;height:52px;display:flex;background:linear-gradient(var(--nav-top),var(--nav-bottom));border-radius:2px}
.nav a{color:#fff;text-decoration:none;font-weight:700;font-size:14px;display:flex;align-items:center;justify-content:center;border-right:1px solid #2c5a88;box-shadow:inset -1px 0 0 rgba(255,255,255,.18)}
.nav a:last-child{border:none;box-shadow:none}
.nav a.current{background:linear-gradient(#3f74a8,#1f4c7c)}
.slider{position:absolute;left:9px;top:195px;width:960px;height:331px;background:#cfcfcf;padding:8px}
.slide{position:relative;width:944px;height:316px;background:linear-gradient(90deg,#eaf4fb,var(--sky));overflow:hidden}
.slide-photo{position:absolute;left:0;top:0;width:500px;height:316px;background:radial-gradient(ellipse at 40% 45%,#e9c6ad 0,#d8ae90 28%,#c9dcea 60%,var(--sky) 100%)}
.testimonial{position:absolute;left:644px;top:22px;width:276px;height:251px;background:rgba(255,255,255,.75);border-radius:3px;padding:14px 24px}
.testimonial h2{color:var(--orange);font-size:17px;text-align:center;padding-bottom:12px;border-bottom:1px solid #d8d8d8;margin:0 -16px}
.testimonial blockquote{font-style:italic;font-size:13px;line-height:24px;color:#666;text-align:justify;margin-top:14px}
.testimonial blockquote b{font-style:normal;font-size:22px;color:#888;font-family:Georgia,serif;vertical-align:-4px}
.testimonial cite{display:block;text-align:right;font-style:normal;font-weight:700;color:var(--blue-dark);font-size:14px;margin-top:6px}
.dots{position:absolute;left:747px;top:288px;display:flex;gap:9px}
.dots i{width:12px;height:12px;border-radius:50%;background:var(--blue);border:2px solid #fff;box-shadow:0 0 1px #999}
.dots i.on{background:var(--orange)}
.cards{position:absolute;left:10px;top:535px;display:flex;gap:16px}
.card{width:309px;height:168px;border-radius:2px;padding:11px 12px;color:#fff;position:relative}
.card.orange{background:linear-gradient(var(--orange-light),var(--orange))}
.card.blue{background:linear-gradient(#6b9ccb,#3572a8)}
.card.slate{background:linear-gradient(var(--slate-top),var(--slate-bottom))}
.card h3{font-size:18px;font-weight:700;letter-spacing:.2px}
.card-photo{position:absolute;left:11px;top:40px;width:106px;height:115px;border:3px solid #fff;border-radius:2px}
.card.orange .card-photo{background:linear-gradient(135deg,#f3e4da,#d9b9a2)}
.card.blue .card-photo{background:linear-gradient(135deg,#d9a76e,#f4e3c8)}
.card.slate .card-photo{background:linear-gradient(135deg,#f1d6c6,#d2a58b)}
.card p{position:absolute;left:126px;top:42px;width:169px;font-size:12px;line-height:18px;text-align:justify}
.card .more{position:absolute;left:126px;top:124px;width:98px;height:30px;background:#fff;color:#777;font-size:14px;display:flex;align-items:center;justify-content:center;border-radius:2px}
.welcome{position:absolute;left:20px;top:726px;width:674px}
.welcome h1{color:var(--orange);font-size:18px;margin-bottom:12px}
.welcome .lead{font-weight:700;font-size:13px;line-height:22px;text-align:justify;color:#222;margin-bottom:8px}
.welcome p{font-size:13px;line-height:22px;text-align:justify;color:#444}
.welcome-photo{position:absolute;left:709px;top:754px;width:255px;height:160px;background:radial-gradient(ellipse at 50% 55%,#d8cbb8 0,#efe7dc 45%,#fff 75%)}
.footer{position:absolute;left:0;top:937px;width:978px;height:92px;background:linear-gradient(var(--footer-top),var(--footer-bottom));color:#bbb;font-size:13px;padding:20px 10px}
.footer nav span{margin:0 8px;color:#999}
.footer .copy{margin-top:15px}
.social{position:absolute;right:9px;top:33px;display:flex;gap:6px}
.social i{width:24px;height:24px;border-radius:3px}
.social i:first-child{background:#3b5a9a}
.social i:last-child{background:#39aadf}
</style>
</head>
<body>
<div class="stage">
  <div class="site">
    <header>
      <div class="brand">
        <span class="brand-mark"></span>
        <span class="brand-name">VELORIN</span>
        <span class="brand-tag">AESTHETICS AND LASER</span>
      </div>
      <div class="search">Search
        <svg width="16" height="16" viewBox="0 0 16 16"><circle cx="6" cy="6" r="4.3" fill="none" stroke="#333" stroke-width="2.2"/><line x1="9" y1="9" x2="14" y2="14" stroke="#333" stroke-width="3" stroke-linecap="round"/></svg>
      </div>
      <div class="contact address">52, Building Name,<br>Street Name, City-Zip code</div>
      <div class="contact lines">Call us : <span class="hl">555 014 2087</span><br>E-mail &nbsp;: <span class="hl">info@velorin-example.com</span></div>
      <nav class="nav">
        <a class="current" style="width:108px">HOME</a>
        <a style="width:144px">ABOUT US</a>
        <a style="width:139px">SERVICES</a>
        <a style="width:238px">LASER PHOTO FACIALS</a>
        <a style="width:175px">TESTIMONIALS</a>
        <a style="width:156px">CONTACT US</a>
      </nav>
    </header>

    <section class="slider">
      <div class="slide">
        <div class="slide-photo" role="img" aria-label="Woman with closed eyes touching her cheek during a facial treatment"></div>
        <div class="testimonial">
          <h2>CLIENT’S TESTIMONIALS</h2>
          <blockquote><b>“</b> Praesent in metus nisi. Ut placerat libero sed urna ornare sit amet iaculis scelerisque ut interdum ac, consequat id neque. Nullam nisl enim, fermentum eleifend sagittis pellentesque, consequat sed orci. <b>”</b></blockquote>
          <cite>Client Name, City</cite>
        </div>
        <div class="dots"><i class="on"></i><i></i><i></i><i></i></div>
      </div>
    </section>

    <section class="cards">
      <article class="card orange">
        <h3>PLUMAVEX CORVANEL</h3>
        <div class="card-photo" role="img" aria-label="Woman receiving a filler injection"></div>
        <p>Integer alcurabitur commodo ipsum eura massa suscipit sit amet varius ligula dictum. Pha sellus tibutristique.</p>
        <a class="more">VIEW MORE</a>
      </article>
      <article class="card blue">
        <h3>LASER PHOTO FACIALS</h3>
        <div class="card-photo" role="img" aria-label="Woman receiving a laser facial treatment"></div>
        <p>Integer alcurabitur commodo ipsum eura massa suscipit sit amet varius ligula dictum. Pha sellus tibutristique.</p>
        <a class="more">VIEW MORE</a>
      </article>
      <article class="card slate">
        <h3>OTHER SERVICES</h3>
        <div class="card-photo" role="img" aria-label="Woman enjoying a face massage"></div>
        <p>Integer alcurabitur commodo ipsum eura massa suscipit sit amet varius ligula dictum. Pha sellus tibutristique.</p>
        <a class="more">VIEW MORE</a>
      </article>
    </section>

    <section class="welcome">
      <h1>WELCOME TO VELORIN</h1>
      <p class="lead">Pellentesque sed turpis mauris, non porttitor purus. Praesent sed feugiat libero. Aenean nec ante massa, et elementum augue. Nunc varius porta iaculis. Maecenas cursus felis a neque blandit tristique.</p>
      <p>Sed elit ipsum, rutrum sit amet ultrices nec, sodales a lorem. Nam in commodo nisl. Morbi a mauris vitae purus facilisis pellentesque. Sed eu massa nibh, quis ultrices orci. Proin cursus, augue a pellentesque laoreet, mauris ipsum varius dui, sit amet tristique metus nibh quis lectus. Aliquam vel mi vitae purus laoreet pretium in sit amet urna. Phasellus vitae feugiat augue. Proin gravida sodales tortor at commodo. Nulla facilisi. Donec faucibus luctus arcu, a iaculis metus mollis et. Morbi facilisis tellus condimentum lectus convallis.</p>
    </section>
    <div class="welcome-photo" role="img" aria-label="Spa still life with rolled towels, soap and a stone bowl"></div>

    <footer class="footer">
      <nav>Home<span>|</span>About us<span>|</span>Services<span>|</span>Laser Photo Facials<span>|</span>Testimonials<span>|</span>Contact us</nav>
      <div class="copy">Copyright &nbsp;© &nbsp;2013 &nbsp;&nbsp; www.velorin-example.com &nbsp;&nbsp;All rights reserved.</div>
      <div class="social"><i></i><i></i></div>
    </footer>
  </div>
</div>
</body>
</html>
```